integrative health clinic-Medical massage, acupuncture, chiropractic

we like our logo, but are open to new ideas. We need a new card design. We have added chiropractic and acupuncture that we have put under the name of the business. We are an integrative medical clinic

Target Market(s)

General public, athletes

Contact Information for Business Card

Phone 5055582917
Fax 5055582916
Hours Monday-Friday 9-6
Saturday 10-6
The 20% can be smaller on the back

Colors
3176b5
0355a3

Requirements
Must have
• Logo but am open to ideas
Nice to have
• We are an integrated medical clinic but also want to be personable. We want the card fun and inviting

```html
<!DOCTYPE html>
<html lang="en">
<head>
<meta charset="utf-8">
<title>Mesa Vital Wellness – Business Card</title>
<link rel="stylesheet" href="https://fonts.googleapis.com/css2?family=EB+Garamond:ital,wght@0,500;0,700;1,500&family=Work+Sans:wght@400;500;600&display=swap">
<style>
  :root {
    --page-bg: #e9eaee;
    --brand-blue: #2f42a0;
    --brand-blue-light: #3c52ad;
    --brand-ink: #26389a;
    --text-dark: #2b2b2b;
    --text-light: #ffffff;
    --card-white: #ffffff;
    --photo-light: #f2f2f2;
    --photo-mid: #a9a9a9;
    --photo-dark: #5c5c5c;
    --divider: #b9c0de;
  }
  * { box-sizing: border-box; margin: 0; padding: 0; }
  html, body { width: 1200px; height: 900px; overflow: hidden; }
  body {
    background: var(--page-bg);
    position: relative;
    font-family: "Work Sans", Arial, sans-serif;
  }
  .card {
    position: absolute;
    left: 250px;
    width: 700px;
    height: 400px;
    border-radius: 22px;
    overflow: hidden;
    box-shadow: 0 10px 28px rgba(0,0,0,.18);
  }

  /* Back of card */
  .card-back {
    top: 36px;
    background: linear-gradient(135deg, var(--brand-blue) 0%, var(--brand-blue-light) 100%);
    color: var(--text-light);
    text-align: center;
  }
  .book-online {
    font-family: "EB Garamond", Georgia, serif;
    font-weight: 700;
    font-size: 30px;
    letter-spacing: .5px;
    margin-top: 38px;
  }
  .brand-lockup {
    display: flex;
    align-items: center;
    justify-content: center;
    gap: 18px;
    margin-top: 18px;
  }
  .brand-mark {
    width: 46px;
    height: 46px;
    border-radius: 50%;
    background: var(--text-light);
  }
  .brand-name {
    font-weight: 500;
    font-size: 50px;
    letter-spacing: -1px;
    line-height: 1;
    white-space: nowrap;
  }
  .brand-tagline {
    font-family: "EB Garamond", Georgia, serif;
    font-style: italic;
    font-size: 27px;
    margin-top: 10px;
    padding-left: 70px;
  }
  .offer {
    font-family: "EB Garamond", Georgia, serif;
    font-weight: 700;
    font-size: 36px;
    letter-spacing: 1.5px;
    margin-top: 34px;
  }
  .insurance-note {
    font-family: "EB Garamond", Georgia, serif;
    font-weight: 500;
    font-size: 22px;
    margin-top: 18px;
  }

  /* Front of card */
  .card-front {
    top: 468px;
    background: var(--card-white);
  }
  .hero-photo {
    position: absolute;
    left: 0; top: 0;
    width: 320px;
    height: 400px;
    background:
      radial-gradient(ellipse 60% 70% at 45% 45%, var(--photo-mid) 0%, transparent 70%),
      linear-gradient(90deg, var(--photo-dark) 0%, var(--photo-mid) 55%, var(--photo-light) 85%, var(--card-white) 100%);
  }
  .front-content {
    position: absolute;
    left: 350px;
    top: 62px;
    right: 16px;
    color: var(--text-dark);
    white-space: nowrap;
  }
  .front-name {
    color: var(--brand-ink);
    font-weight: 600;
    font-size: 30px;
    letter-spacing: .3px;
    line-height: 1.1;
  }
  .front-services {
    font-size: 20px;
    font-weight: 400;
    line-height: 1.15;
    margin-top: 2px;
    letter-spacing: .3px;
  }
  .front-services small {
    display: block;
    font-size: 17px;
  }
  .specialty {
    font-size: 16px;
    line-height: 1.3;
    margin-top: 16px;
  }
  .contact-list {
    list-style: none;
    margin-top: 16px;
    border-left: 1.5px solid var(--divider);
    padding-left: 14px;
    position: relative;
  }
  .contact-item {
    position: relative;
    font-size: 16px;
    line-height: 1.5;
  }
  .contact-item svg {
    position: absolute;
    left: -36px;
    top: 4px;
    width: 15px;
    height: 15px;
    fill: none;
    stroke: var(--brand-ink);
    stroke-width: 2;
  }
  .contact-item .pin { fill: var(--brand-ink); stroke: none; }
  .web-domain { color: var(--brand-ink); }
</style>
</head>
<body>

<section class="card card-back" aria-label="Card back">
  <p class="book-online">Book Online</p>
  <div class="brand-lockup">
    <span class="brand-mark" aria-hidden="true"></span>
    <span class="brand-name">Mesa Vital Wellness</span>
  </div>
  <p class="brand-tagline">Sports Therapy and Wellness Center</p>
  <p class="offer">20% OFF FIRST VISIT</p>
  <p class="insurance-note">We accept some insurances, Worker's Comp and Personal Injury.</p>
</section>

<section class="card card-front" aria-label="Card front">
  <div class="hero-photo" role="img" aria-label="Photo of a man's bare back, hands on neck and lower back, with a highlighted spine showing pain points"></div>
  <div class="front-content">
    <h1 class="front-name">Mesa Vital Wellness</h1>
    <p class="front-services">Medical and Sports Massage<small>chiropractic and acupuncture</small></p>
    <p class="specialty">Specializing in Medical, Sports Massage<br>and Manual Therapies</p>
    <ul class="contact-list">
      <li class="contact-item">
        <svg viewBox="0 0 16 16" aria-hidden="true"><path d="M4 1.5l2.5 3-1.5 1.8c.8 1.8 2.4 3.4 4.2 4.2L11 9l3 2.5-1.3 2.5C7 13.5 2.5 9 2 3.3z"/></svg>
        (505) 558-2917
      </li>
      <li class="contact-item">
        <svg viewBox="0 0 16 16" aria-hidden="true"><rect x="1.5" y="3.5" width="13" height="9" rx="1"/><path d="M1.5 4l6.5 5 6.5-5"/></svg>
        info@mesavitalnm.com
      </li>
      <li class="contact-item">
        <svg viewBox="0 0 16 16" aria-hidden="true"><path class="pin" d="M8 0.5a5 5 0 0 0-5 5c0 4 5 10 5 10s5-6 5-10a5 5 0 0 0-5-5zm0 7a2 2 0 1 1 0-4 2 2 0 0 1 0 4z"/></svg>
        418 Alameda Row, B3 Santa Fe. NM 87501
      </li>
      <li class="contact-item">
        <svg viewBox="0 0 16 16" aria-hidden="true"><circle cx="8" cy="8" r="6.5"/><ellipse cx="8" cy="8" rx="3" ry="6.5"/><path d="M1.5 8h13M2.5 4.8h11M2.5 11.2h11"/></svg>
        www.<span class="web-domain">mesavitalnm</span>.com
      </li>
    </ul>
  </div>
</section>

</body>
</html>
```